Business card design needed to incorporate existing logo

We need a business card for a new modern Accounting & Business Solutions company call KelvaTrade Services.com.au servicing all of Australia.
My tagline is Steady Ledger Answers... built right.

We specialise in Cloud Accounting and this is our primary focus. We also provide tax representation, debt recovery, computer, tablet and smart phone sales.

I would like a design that uses my corporate, trustworthy colours of blue/white, black/grey however am open to suggestion. I have attached my logo to go on the card somewhere,of which you will see the colour scheme.

I am after a card that STANDS OUT, somewhere between it not being too busy and not being a baron waste of space.

A 'cloud' incorporated in the design may work well, up to your artistic judgement. I know what I like when I see it; it is harder to put into words!

Excited to see your ideas!
I have added my logo predominately (blue/white) and for additional opportunity have added my reverse logo (darker one). I have used the blue/white on my website and letterhead. I will be using both on my vehicle signage.

Target Market(s)

Tradesmen and small-medium businesses of all descriptions Australia-wide

Industry/Entity Type

Debt

Contact Information for Business Card

Dale Pemberton
Principal (optional)
KelvaTrade Services.com.au
Steady Ledger Answers... built right

P: 1800 513 684
M: 0412 860 571 (optional)
W: www.kelvatradeservices.com.au
E: admin@kelvatradeservices.com.au

Logo Text

Steady Ledger Answers... built right!

Logo styles of interest
Wordmark Logo
Requirements
Must have
• Must look professional and of high quality not cheap.

My logo and my tagline 'Steady Ledger Answers... built right'.

I have my colourscheme in mind as per my attached logo, however am open to suggestion. I want to see what you can create that I would not have thought of.

Modern, innovative.
Something I won't look at and think, 'I could have done that myself'.

Must be able to be printed on Norla 300gm premium cards and the artwork provided to me.
Nice to have
• Title of Principal is optional depending on space and judement call of look/fee.
M: (mobile) number is also optional as above.

Somthing cloud related given the Cloud Accounting aspect may be relevant. I leave it to your artistic design and judgement.
Should not have
• Must not look cheap.

```html
<!DOCTYPE html>
<html lang="en">
<head>
<meta charset="utf-8">
<title>KelvaTrade Services – Business Card</title>
<link rel="stylesheet" href="https://fonts.googleapis.com/css2?family=Cabin:wght@400;500&display=swap">
<style>
  :root {
    --navy: #1b2756;
    --sky: #1577bd;
    --sky-light: #3a9ad6;
    --steel: #8b93ad;
    --paper: #ffffff;
    --ink: #1d2240;
    --stage-light: #f4f4f4;
    --stage-dark: #9a9a9a;
  }
  * { box-sizing: border-box; margin: 0; padding: 0; }
  html, body { width: 1200px; height: 900px; overflow: hidden; }
  body {
    position: relative;
    background: radial-gradient(ellipse at 50% 45%, var(--stage-light) 0%, #d9d9d9 55%, var(--stage-dark) 100%);
    font-family: "Cabin", "Gill Sans", sans-serif;
  }
  .card {
    position: absolute;
    width: 560px;
    height: 320px;
    overflow: hidden;
    box-shadow: 0 6px 18px rgba(0,0,0,0.25);
  }

  /* Back of card */
  .card-back { left: 320px; top: 110px; background: var(--navy); }
  .card-back .emblem-area {
    position: absolute; left: 0; top: 0; width: 250px; height: 320px;
    background: linear-gradient(135deg, #9aa1b9 0%, var(--steel) 100%);
    border-top-right-radius: 160px 160px;
    border-bottom-right-radius: 160px 160px;
  }
  .card-back .wordmark {
    position: absolute; left: 280px; top: 118px;
    color: var(--sky-light);
  }

  /* Wordmark */
  .wordmark { font-weight: 400; line-height: 1; }
  .wordmark .name { display: block; font-size: 40px; letter-spacing: 2px; text-transform: uppercase; }
  .wordmark .sub { display: block; font-size: 17px; letter-spacing: 5px; text-transform: uppercase; margin-top: 4px; }

  /* Front of card */
  .card-front { left: 330px; top: 470px; background: var(--paper); }
  .card-front .waves { position: absolute; inset: 0; }
  .card-front .wordmark { position: absolute; left: 26px; top: 36px; color: var(--sky); }
  .card-front .wordmark .name { font-size: 36px; }
  .card-front .wordmark .sub { font-size: 15px; letter-spacing: 4px; }

  .contact { position: absolute; left: 352px; top: 44px; color: var(--ink); }
  .contact .person { font-size: 17px; letter-spacing: 0.5px; text-transform: uppercase; }
  .contact .role { font-size: 11px; letter-spacing: 1px; text-transform: uppercase; margin-bottom: 10px; }
  .contact ul { list-style: none; }
  .contact li { display: flex; align-items: center; gap: 6px; font-size: 11.5px; line-height: 16px; }
  .contact .icon { width: 11px; height: 11px; background: var(--navy); border-radius: 2px; display: inline-flex; }
  .contact .icon svg { width: 11px; height: 11px; }

  .tagline {
    position: absolute; left: 56px; bottom: 40px;
    color: #e8ecf7; font-size: 16px; letter-spacing: 1px; text-transform: uppercase;
  }
</style>
</head>
<body>

<section class="card card-back" aria-label="Card back">
  <div class="emblem-area" role="img" aria-label="Large globe emblem with map of Australia"></div>
  <div class="wordmark">
    <span class="name">KelvaTrade</span>
    <span class="sub">Services.com.au</span>
  </div>
</section>

<section class="card card-front" aria-label="Card front">
  <svg class="waves" viewBox="0 0 560 320" preserveAspectRatio="none" aria-hidden="true">
    <path d="M0 200 C 90 160, 200 175, 270 205 C 360 180, 470 170, 560 175 L560 320 L0 320 Z" fill="var(--navy)"/>
    <path d="M0 142 C 70 190, 200 200, 300 178 C 220 200, 110 200, 0 176 Z" fill="var(--sky)"/>
    <path d="M180 198 C 290 150, 450 160, 560 178 L560 186 C 450 172, 300 175, 230 210 Z" fill="var(--sky)"/>
  </svg>

  <div class="wordmark">
    <span class="name">KelvaTrade</span>
    <span class="sub">Services.com.au</span>
  </div>

  <div class="contact">
    <p class="person">Dale Pemberton</p>
    <p class="role">Principal</p>
    <ul>
      <li><span class="icon"><svg viewBox="0 0 11 11"><path d="M3 2 L4.5 2 L5 4 L4 4.6 Q4.8 6.3 6.4 7 L7 6 L9 6.5 L9 8 Q5 9 2.5 4.5 Z" fill="#fff"/></svg></span>1800 513 684</li>
      <li><span class="icon"><svg viewBox="0 0 11 11"><rect x="3.5" y="1.5" width="4" height="8" rx="0.8" fill="none" stroke="#fff" stroke-width="1"/></svg></span>0412 860 571</li>
      <li><span class="icon"><svg viewBox="0 0 11 11"><circle cx="5.5" cy="5.5" r="3.5" fill="none" stroke="#fff" stroke-width="0.9"/><path d="M2 5.5 H9 M5.5 2 V9" stroke="#fff" stroke-width="0.7"/></svg></span>www.kelvatradeservices.com.au</li>
    </ul>
  </div>

  <p class="tagline">Steady Ledger Answers... built right</p>
</section>

</body>
</html>
```